Wildlife photographer Website

The website is to be a "resume" of pictures and awards won by Nora. Lean heavy to outdoor wildlife.
She will post articles and have ability to interact with fans.

I will add some of her pictures tonight,

Target Market(s)

Terra Quarterly .....anyone looking to hire a wildlife photographer.

Industry/Entity Type

Professional Photography

Contact Information for Business Card

Nora Falkett
4817 Maple Hollow Lane
Columbia MD 21078
443-581-2094
Nora@FernOwlPix.com

Coding

Coded - Design and coding required

Number of Pages Required

5+ page

Requirements
Must have
• New Logo
Nice to have
• Nature, and eye catching graphics

```html
<!DOCTYPE html>
<html lang="en">
<head>
<meta charset="utf-8">
<title>Nora Falkett – Wildlife Photographer</title>
<link rel="stylesheet" href="https://fonts.googleapis.com/css2?family=Mulish:wght@400;600;700&family=Roboto+Condensed:wght@400;500&display=swap">
<style>
:root{
  --yellow:#fcd02a;
  --ink:#1d1d1d;
  --text:#333333;
  --band:#e8e9eb;
  --footer:#333333;
  --footer-text:#e6e6e6;
  --white:#ffffff;
}
*{margin:0;padding:0;box-sizing:border-box}
html,body{width:1200px;height:4015px;overflow:hidden}
body{position:relative;background:var(--white);font-family:"Mulish",sans-serif;color:var(--text)}
.abs{position:absolute}
.btn{position:absolute;background:var(--yellow);color:var(--ink);font-family:"Roboto Condensed",sans-serif;font-size:18px;display:flex;align-items:center;justify-content:center;border-radius:3px}
.cond{font-family:"Roboto Condensed",sans-serif}

/* header */
.site-header{left:0;top:0;width:1200px;height:100px;background:var(--white)}
.brand-mark{left:160px;top:15px;width:76px;height:76px;border-radius:50%;background:var(--ink)}
.brand-name{left:246px;top:18px;font-size:38px;line-height:40px;color:var(--ink)}
.brand-sub{left:248px;top:56px;font-size:21px;color:var(--ink)}
.main-nav a{position:absolute;top:42px;font-family:"Roboto Condensed",sans-serif;font-size:17px;color:var(--ink);text-decoration:none}
.header-hire{left:915px;top:31px;width:123px;height:44px;font-size:21px}

/* hero */
.hero{left:0;top:100px;width:1200px;height:504px;background:linear-gradient(100deg,#2a2a22 0%,#3b3a2c 35%,#5a4a35 60%,#8a5a34 75%,#3a3426 100%)}
.hero-panel{left:162px;top:222px;width:398px;height:262px;background:rgba(30,30,25,.55);border-left:6px solid var(--yellow)}
.hero-kicker{left:198px;top:272px;font-size:22px;color:var(--white)}
.hero-title{left:198px;top:302px;font-size:38px;color:var(--white)}
.hero-by{left:198px;top:348px;font-size:22px;color:var(--white)}
.hero-hire{left:198px;top:390px;width:122px;height:42px;font-size:20px}

/* intro */
.section-title{width:1200px;left:0;text-align:center;font-size:32px;color:var(--ink)}
.intro-text{left:195px;top:710px;width:810px;text-align:center;font-size:13px;line-height:24px}

/* projects */
.band{left:0;width:1200px;background:var(--band)}
.photo{position:absolute;width:286px;height:206px}
.project-title{font-size:26px;color:var(--ink);line-height:32px}
.project-text{font-size:13px;line-height:24.5px;width:268px}
.gallery-btn{width:124px;height:42px}

/* about */
.about{left:0;top:2563px;width:1200px;height:467px;background:linear-gradient(90deg,#e9ded2,#efe6dc 50%,#e6ddd0)}
.about-portrait{left:168px;top:2640px;width:322px;height:322px;border-radius:50%;border:3px solid var(--yellow);padding:8px;background:var(--white)}
.about-portrait div{width:100%;height:100%;border-radius:50%;background:linear-gradient(160deg,#6f7f7a,#3f8aa0 55%,#b56a3a)}
.about-title{left:522px;top:2660px;font-size:28px;color:var(--ink)}
.about-text{left:524px;top:2704px;width:518px;font-size:13px;line-height:24.5px}
.about-btn{left:525px;top:2883px;width:188px;height:43px}

/* articles */
.article{position:absolute;left:162px;width:402px;height:74px;border-bottom:1px solid #cfcfcf}
.article .date{position:absolute;top:0;font-size:14px;color:var(--ink)}
.article .line{position:absolute;top:26px;font-size:13px}
.article .arrow{position:absolute;right:4px;top:26px;width:16px;height:16px}
.articles-photo{left:615px;top:3168px;width:423px;height:330px;background:linear-gradient(170deg,#6e7a5a,#a07258 50%,#8a5a44)}
.more-btn{left:160px;top:3452px;width:106px;height:44px}

/* footer */
.site-footer{left:0;top:3630px;width:1200px;height:385px}
.footer-mark{left:545px;top:3595px;width:110px;height:110px;border-radius:50%;background:var(--footer);border:4px solid var(--white)}
.footer-name{left:0;width:1200px;text-align:center;top:3700px;font-size:32px;color:var(--white)}
.footer-sub{left:0;width:1200px;text-align:center;top:3736px;font-size:20px;color:var(--white)}
.footer-nav a{position:absolute;top:3785px;font-size:15px;color:var(--footer-text);text-decoration:none}
.footer-rule{left:162px;top:3835px;width:876px;height:1px;background:#555}
.contact-icon{position:absolute;width:48px;height:48px;border-radius:50%;background:var(--yellow)}
.contact-label{position:absolute;font-size:14px;font-weight:700;color:var(--white)}
.contact-value{position:absolute;font-size:13px;color:var(--footer-text);line-height:17px}
.copyright{left:162px;top:3965px;font-size:12px;color:var(--footer-text)}
.social{position:absolute;top:3958px;width:28px;height:28px;border-radius:50%;background:var(--yellow)}
</style>
</head>
<body>

<header class="abs site-header">
  <div class="abs brand-mark"></div>
  <div class="abs brand-name">Nora Falkett</div>
  <div class="abs brand-sub cond">Wildlife Photographer</div>
  <nav class="main-nav">
    <a style="left:620px">About Me</a>
    <a style="left:729px">My Gallery</a>
    <a style="left:842px">Articles</a>
  </nav>
  <div class="btn header-hire">Hire Me</div>
</header>

<section class="abs hero" role="img" aria-label="Red fox sitting among fallen branches and bamboo stalks"></section>
<div class="abs hero-panel"></div>
<div class="abs hero-kicker">Welcome to</div>
<div class="abs hero-title">Wildlife Photography</div>
<div class="abs hero-by">By Nora Falkett</div>
<div class="btn hero-hire">Hire Me</div>

<h1 class="abs section-title" style="top:660px;font-weight:400">Featured Photography Projects</h1>
<p class="abs intro-text">I <b style="color:var(--ink)">have listed my 3 recents project or visited place below</b> lorem ipsum dolor sit amet, consectetuer adipiscing elit, sed diam nonummy nibh euismod tincidunt ut laoreet dolore magna aliquam erat volutpat. Ut wisi enim ad minim veniam, quis nostrud exerci tation ullamcorper suscipit lobortis nisl ut aliquip ex ea commodo consequat. Duis autem vel eum iriure dolor.</p>

<!-- project one -->
<section class="abs band" style="top:831px;height:577px"></section>
<div class="photo" style="left:162px;top:906px;background:linear-gradient(180deg,#9a8c7a,#c7b49a)" role="img" aria-label="Sanderling standing on wet sand"></div>
<div class="photo" style="left:458px;top:906px;background:linear-gradient(180deg,#3d5a6e,#2a4356)" role="img" aria-label="Long-tailed duck swimming"></div>
<div class="photo" style="left:162px;top:1127px;background:linear-gradient(180deg,#9aa3a8,#b48f52)" role="img" aria-label="Flock of buntings flying over grass"></div>
<div class="photo" style="left:458px;top:1127px;background:linear-gradient(180deg,#334a58,#5f7f96)" role="img" aria-label="Great blue heron in flight over water"></div>
<h2 class="abs project-title" style="left:767px;top:980px;font-weight:400">Lorem Ispum</h2>
<p class="abs project-text" style="left:768px;top:1025px">Lorem ipsum dolor sit amet, consectetuer adipiscing elit, sed diam nonummy nibh euismod tincidunt ut laoreet dlore magna aliquam erat volutpat. Ut wisifd fenim ad minim veniam, quis nostrud exerci tation ullamcorper suscipit lobortis nisl ut aliquip ex ea commodo consequat duis.</p>
<div class="btn gallery-btn" style="left:768px;top:1210px">View Gallery</div>

<!-- project two -->
<h2 class="abs project-title" style="left:160px;top:1560px;font-weight:400">Lorem Ispum</h2>
<p class="abs project-text" style="left:162px;top:1605px">Lorem ipsum dolor sit amet, consectetuer adipiscing elit, sed diam nonummy nibh euismod tincidunt ut laoreet dlore magna aliquam erat volutpat. Ut wisifd fenim ad minim veniam, quis nostrud exerci tation ullamcorper suscipit lobortis nisl ut aliquip ex ea commodo consequat duis.</p>
<div class="btn gallery-btn" style="left:162px;top:1782px">View Gallery</div>
<div class="photo" style="left:454px;top:1483px;background:linear-gradient(180deg,#5d6f86,#e0a33c 55%,#5a4a3a)" role="img" aria-label="Sunset over a gravel road"></div>
<div class="photo" style="left:751px;top:1483px;background:linear-gradient(180deg,#7b8f96,#5d5346)" role="img" aria-label="Duck stretching its wings on water"></div>
<div class="photo" style="left:454px;top:1705px;background:linear-gradient(180deg,#a37a3a,#6a4a22)" role="img" aria-label="River otter in golden water"></div>
<div class="photo" style="left:751px;top:1705px;background:linear-gradient(180deg,#3f4f58,#b98a4a)" role="img" aria-label="Wave breaking at golden hour"></div>

<!-- project three -->
<section class="abs band" style="top:1985px;height:578px"></section>
<div class="photo" style="left:162px;top:2061px;background:linear-gradient(180deg,#3b3a2c,#8a5a34)" role="img" aria-label="Red fox sitting near bamboo"></div>
<div class="photo" style="left:458px;top:2061px;background:linear-gradient(180deg,#2c3a52,#c9d2de)" role="img" aria-label="Rabbit leaping over snow"></div>
<div class="photo" style="left:162px;top:2282px;background:linear-gradient(180deg,#e8ecf0,#c9a06a)" role="img" aria-label="Female cardinal in snow"></div>
<div class="photo" style="left:458px;top:2282px;background:linear-gradient(180deg,#c8c2b4,#8f9a82)" role="img" aria-label="Hummingbird hovering near water"></div>
<h2 class="abs project-title" style="left:768px;top:2115px;font-weight:400">Remote &amp; Camera<br>Trap Photography</h2>
<p class="abs project-text" style="left:768px;top:2196px">Lorem ipsum dolor sit amet, consectetuer adipiscing elit, sed diam nonummy nibh euismod tincidunt ut laoreet dlore magna aliquam erat volutpat. Ut wisifd fenim ad minim veniam, quis nostrud exerci tation ullamcorper suscipit lobortis nisl ut aliquip ex ea commodo consequat duis.</p>
<div class="btn gallery-btn" style="left:768px;top:2380px">View Gallery</div>

<!-- about -->
<section class="abs about" role="img" aria-label="Faded background of the photographer lying on the ground outdoors"></section>
<div class="abs about-portrait"><div role="img" aria-label="Portrait of Nora Falkett outdoors by a river"></div></div>
<h2 class="abs about-title" style="font-weight:400">About Nora Falkett</h2>
<p class="abs about-text">Lorem ipsum dolor sit amet, consectetuer adipiscing elit, sed diam nonummy nibh euismod tincidunt ut laoreet dlore magna aliquam erat volutpat. Ut wisifd fenim ad minim veniam, quis nostrud exerci tation ullamcorper suscipit lobortis nisl ut aliquip ex ea commodo consequat duis. Lorem ipsum dolor sit amet, consectetuer adipiscing elit, sed diam nonummy nibh euismod tincidunt ut laoreet dlore magna aliquam erat volutpat. Ut wisifd fenim ad minim veniam, quis nostrud exerci tation ullamcorper suscipit lobortis nisl ut aliquip.</p>
<div class="btn about-btn">Read More About Me</div>

<!-- articles -->
<h2 class="abs section-title" style="top:3098px;font-size:28px;font-weight:400">Recent Articles</h2>
<div class="article" style="top:3164px"><span class="date">Mar, 03 2021</span><span class="line">Lorem ipsum dolor sit amet, consectetuer adipiscing sed</span><svg class="arrow" viewBox="0 0 16 16"><circle cx="8" cy="8" r="7" fill="none" stroke="#fcd02a" stroke-width="1.3"/><path d="M7 5l3 3-3 3" fill="none" stroke="#fcd02a" stroke-width="1.3"/></svg></div>
<div class="article" style="top:3238px"><span class="date">Mar, 05 2021</span><span class="line">Lorem ipsum dolor sit amet, consectetuer adipiscing sed</span><svg class="arrow" viewBox="0 0 16 16"><circle cx="8" cy="8" r="7" fill="none" stroke="#fcd02a" stroke-width="1.3"/><path d="M7 5l3 3-3 3" fill="none" stroke="#fcd02a" stroke-width="1.3"/></svg></div>
<div class="article" style="top:3312px"><span class="date">Mar, 08 2021</span><span class="line">Lorem ipsum dolor sit amet, consectetuer adipiscing sed</span><svg class="arrow" viewBox="0 0 16 16"><circle cx="8" cy="8" r="7" fill="none" stroke="#fcd02a" stroke-width="1.3"/><path d="M7 5l3 3-3 3" fill="none" stroke="#fcd02a" stroke-width="1.3"/></svg></div>
<div class="article" style="top:3384px;border-bottom:none"><span class="date">Mar, 08 2021</span><span class="line">Lorem ipsum dolor sit amet, consectetuer adipiscing sed</span><svg class="arrow" viewBox="0 0 16 16"><circle cx="8" cy="8" r="7" fill="none" stroke="#fcd02a" stroke-width="1.3"/><path d="M7 5l3 3-3 3" fill="none" stroke="#fcd02a" stroke-width="1.3"/></svg></div>
<div class="btn more-btn">View More</div>
<div class="abs articles-photo" role="img" aria-label="Photographer hiking with trekking poles among pine trees"></div>

<!-- footer -->
<svg class="abs site-footer" viewBox="0 0 1200 385" preserveAspectRatio="none">
  <path d="M0 160 Q600 -60 1200 160 L1200 385 L0 385 Z" fill="#333333"/>
  <path d="M0 160 Q600 -60 1200 160" fill="none" stroke="#fcd02a" stroke-width="5"/>
</svg>
<div class="abs footer-mark"></div>
<div class="abs footer-name">Nora Falkett</div>
<div class="abs footer-sub cond">Wildlife Photographer</div>
<nav class="footer-nav">
  <a style="left:371px">Home</a>
  <a style="left:454px">About Me</a>
  <a style="left:563px">My Gallery</a>
  <a style="left:681px">Articles</a>
  <a style="left:775px">Hire Me</a>
</nav>
<div class="abs footer-rule"></div>

<div class="contact-icon" style="left:181px;top:3866px"><svg viewBox="0 0 48 48" width="48" height="48"><path d="M18 15c2 0 3 4 3 5s-2 2-2 3 4 6 6 7c1 0 2-2 3-2s5 1 5 3-2 4-4 4c-6 0-15-9-15-16 0-2 2-4 4-4z" fill="none" stroke="#333" stroke-width="1.6"/></svg></div>
<div class="contact-label" style="left:245px;top:3866px">PHONE</div>
<div class="contact-value" style="left:245px;top:3888px">443-581-2094</div>

<div class="contact-icon" style="left:466px;top:3866px"><svg viewBox="0 0 48 48" width="48" height="48"><path d="M24 13c-5 0-8 4-8 8 0 6 8 14 8 14s8-8 8-14c0-4-3-8-8-8z" fill="none" stroke="#333" stroke-width="1.6"/><circle cx="24" cy="21" r="3" fill="none" stroke="#333" stroke-width="1.6"/></svg></div>
<div class="contact-label" style="left:531px;top:3866px">ADDRESS</div>
<div class="contact-value" style="left:531px;top:3888px;font-size:12px">4817 Maple Hollow Lane<br>Columbia MD 21078</div>

<div class="contact-icon" style="left:821px;top:3866px"><svg viewBox="0 0 48 48" width="48" height="48"><rect x="14" y="17" width="20" height="14" fill="none" stroke="#333" stroke-width="1.6"/><path d="M14 17l10 8 10-8" fill="none" stroke="#333" stroke-width="1.6"/></svg></div>
<div class="contact-label" style="left:883px;top:3866px">EMAIL</div>
<div class="contact-value" style="left:883px;top:3888px">Nora@FernOwlPix.com</div>

<div class="abs copyright">Copyright © 2021 Nora Falkett Wildlife Photographer. All Rights Reserved.</div>
<div class="social" style="left:902px"></div>
<div class="social" style="left:938px"></div>
<div class="social" style="left:974px"></div>
<div class="social" style="left:1010px"></div>

</body>
</html>
```